Brennick Holdings Business Cards

These are professional business cards that are for my family office.
Put fake emails and phone numbers as of now until I finalize those components. This family office controls my families investments, assets, and future. The cards should be professional.
..
.
.
.
I just uploaded another variation of a logo I would like to see as a business card to I am inbeteen which logo to use

Target Market(s)

business

Industry/Entity Type

business

Contact Information for Business Card

Professional, wealth related, finance related.

Requirements
Must have
• Logo

```html
<!DOCTYPE html>
<html lang="en">
<head>
<meta charset="utf-8">
<title>Brennick Holdings – Business Cards</title>
<link href="https://fonts.googleapis.com/css2?family=Cinzel:wght@500;600&family=Libre+Baskerville:wght@400;700&display=swap" rel="stylesheet">
<style>
  :root {
    --navy: #181d2b;
    --paper: #ffffff;
    --ink: #1c2130;
    --grey-dot: #a9a9a9;
    --faint: #e8e8e8;
    --backdrop: #e9eaec;
    --muted: #555a66;
  }
  * { margin: 0; padding: 0; box-sizing: border-box; }
  html, body { width: 1200px; height: 800px; overflow: hidden; }
  body {
    background: var(--backdrop);
    position: relative;
    font-family: "Libre Baskerville", Georgia, serif;
  }
  .card {
    position: absolute;
    top: 250px;
    width: 520px;
    height: 300px;
    overflow: hidden;
    box-shadow: 0 10px 30px rgba(0,0,0,0.12);
  }
  .card svg.card-lines { position: absolute; inset: 0; }

  /* Back card */
  .card-back { left: 50px; background: var(--navy); color: var(--paper); }
  .card-back .website {
    position: absolute; left: 34px; top: 34px;
    font-size: 11px; letter-spacing: 4.5px;
  }
  .card-back .brand-name {
    position: absolute; right: 28px; top: 196px;
    font-family: "Cinzel", serif; font-weight: 500;
    font-size: 30px; letter-spacing: 1px;
  }

  /* Front card */
  .card-front { left: 630px; background: var(--paper); color: var(--ink); }
  .card-front .person { position: absolute; left: 40px; top: 44px; }
  .card-front .person-name {
    font-weight: 700; font-size: 15px; letter-spacing: 0.5px;
  }
  .card-front .person-role {
    font-size: 10px; color: var(--muted); margin-top: 3px;
    padding-bottom: 3px; border-bottom: 1px solid #999; display: inline-block; padding-right: 14px;
  }
  .contact-list { position: absolute; left: 40px; top: 112px; list-style: none; }
  .contact-list li {
    display: flex; align-items: center; gap: 7px;
    font-size: 11px; height: 21px;
  }
  .contact-list svg { width: 11px; height: 11px; fill: var(--ink); }
  .address {
    position: absolute; left: 232px; top: 154px;
    font-size: 11px; line-height: 18px;
    padding-left: 12px; border-left: 1px solid #888;
  }
  .brand-lockup {
    position: absolute; right: 26px; top: 50px;
    display: flex; flex-direction: column; align-items: center; gap: 10px;
  }
  .brand-lockup .mark-circle {
    width: 62px; height: 62px; border: 2px solid var(--ink); border-radius: 50%;
    background: var(--paper);
  }
  .brand-lockup .brand-name {
    font-family: "Cinzel", serif; font-weight: 600; font-size: 14px; letter-spacing: 0.5px;
    color: var(--ink); white-space: nowrap;
  }
</style>
</head>
<body>

  <section class="card card-back" aria-label="Business card back">
    <svg class="card-lines" width="520" height="300" viewBox="0 0 520 300">
      <line x1="0" y1="168" x2="22" y2="168" stroke="#fff" stroke-width="2"/>
      <g fill="var(--grey-dot)">
        <circle cx="34" cy="168" r="5"/><circle cx="48" cy="168" r="5"/><circle cx="62" cy="168" r="5"/>
        <circle cx="76" cy="168" r="5"/><circle cx="90" cy="168" r="5"/>
      </g>
      <line x1="102" y1="168" x2="170" y2="168" stroke="#fff" stroke-width="2"/>
      <g fill="var(--grey-dot)">
        <circle cx="452" cy="188" r="3"/><circle cx="462" cy="188" r="3"/><circle cx="472" cy="188" r="3"/>
        <circle cx="482" cy="188" r="3"/><circle cx="492" cy="188" r="3"/>
      </g>
      <line x1="80" y1="252" x2="520" y2="252" stroke="#fff" stroke-width="2"/>
    </svg>
    <p class="website">www.brennickholdings.com</p>
    <h2 class="brand-name">Brennick Holdings</h2>
  </section>

  <section class="card card-front" aria-label="Business card front">
    <svg class="card-lines" width="520" height="300" viewBox="0 0 520 300">
      <circle cx="270" cy="10" r="112" fill="none" stroke="var(--faint)" stroke-width="6"/>
      <line x1="0" y1="206" x2="360" y2="206" stroke="var(--ink)" stroke-width="2"/>
      <g fill="var(--grey-dot)">
        <circle cx="378" cy="228" r="5"/><circle cx="392" cy="228" r="5"/><circle cx="406" cy="228" r="5"/>
        <circle cx="420" cy="228" r="5"/><circle cx="434" cy="228" r="5"/>
      </g>
      <line x1="446" y1="250" x2="520" y2="250" stroke="var(--ink)" stroke-width="2"/>
    </svg>

    <div class="person">
      <h1 class="person-name">GRAHAM ELLERY</h1>
      <p class="person-role">Director</p>
    </div>

    <ul class="contact-list">
      <li><svg viewBox="0 0 24 24"><path d="M6.6 10.8a15 15 0 0 0 6.6 6.6l2.2-2.2a1 1 0 0 1 1-.25 11.4 11.4 0 0 0 3.6.57 1 1 0 0 1 1 1V20a1 1 0 0 1-1 1A17 17 0 0 1 3 4a1 1 0 0 1 1-1h3.5a1 1 0 0 1 1 1c0 1.25.2 2.45.57 3.57a1 1 0 0 1-.25 1z"/></svg>300-555-0142</li>
      <li><svg viewBox="0 0 24 24"><path d="M2 5h20v14H2z M3 6l9 7 9-7" fill="none" stroke="currentColor" stroke-width="2"/></svg>info@brennickholdings.com</li>
      <li><svg viewBox="0 0 24 24"><g fill="none" stroke="currentColor" stroke-width="2"><circle cx="12" cy="12" r="10"/><path d="M2 12h20M12 2c3 3 3 17 0 20M12 2c-3 3-3 17 0 20"/></g></svg>www.brennickholdings.com</li>
    </ul>

    <p class="address">00 dummy city<br>dummy place 0000</p>

    <div class="brand-lockup">
      <span class="mark-circle" aria-hidden="true"></span>
      <span class="brand-name">Brennick Holdings</span>
    </div>
  </section>

</body>
</html>
```